Business card design needed

I need a business card for my new business.
I make environmentally friendly candles from all natural premium ingredients.
The candles are hand-poured locally in Melbourne, Australia.
I also want my card to match my website www.velmirawicks.com.au (similar colours, font). Can add additional fonts to create more interest...
I want my design to reflect class and simplicity.
Target Market(s)
Target audience 25-50
The candles represent luxury but need to appeal to the environmentally conscious...
Needs to appeal to both men and women. A luxury gift a man would buy for his girlfriend or mother or for his home and for a woman it needs to represent quality...
Industry/Entity Type
Business
Contact Information for Business Card
Velmira Candles
Hand-Poured Eco Soy Candles
Lorraine Quibell - Founder
0438 276 904
www.velmirawicks.com.au
Logo Text
VELMIRA
Logo styles of interest
Wordmark Logo
Look and feel
Each slider illustrates characteristics of the customer's brand and the style your logo design should communicate.

```html
<!DOCTYPE html>
<html lang="en">
<head>
<meta charset="utf-8">
<title>Velmira Candles — Business Card</title>
<link rel="stylesheet" href="https://fonts.googleapis.com/css2?family=Roboto+Slab:wght@300;400;500&display=swap">
<style>
  :root {
    --stage: #3b3b3c;
    --card-light: #dcdcda;
    --card-dark: #2b2b2c;
    --ink-dark: #2a2a2b;
    --ink-light: #dcdcda;
    --mint: #a8cdca;
    --font-slab: "Roboto Slab", "Rockwell", serif;
  }
  * { box-sizing: border-box; margin: 0; padding: 0; }
  html, body {
    width: 1200px;
    height: 900px;
    overflow: hidden;
    background: var(--stage);
    font-family: var(--font-slab);
  }
  .stage {
    width: 1200px;
    height: 900px;
    display: flex;
    flex-direction: column;
    align-items: center;
    justify-content: center;
    gap: 44px;
  }
  .card {
    width: 700px;
    height: 400px;
    position: relative;
    box-shadow: 0 14px 30px rgba(0, 0, 0, 0.35);
  }
  .card--front { background: var(--card-light); color: var(--ink-dark); }
  .card--back { background: var(--card-dark); color: var(--mint); }

  .card__content {
    position: absolute;
    left: 150px;
    top: 118px;
  }
  .card--back .card__content { top: 140px; }

  .wordmark {
    display: flex;
    align-items: center;
    gap: 14px;
    font-weight: 400;
    font-size: 40px;
    letter-spacing: 1px;
    line-height: 1;
    text-transform: uppercase;
  }
  .wordmark__square {
    width: 22px;
    height: 22px;
    flex: none;
  }
  .card--front .wordmark__square { background: var(--ink-dark); }
  .card--back .wordmark__square { background: var(--mint); }

  .tagline {
    margin: 14px 0 0 36px;
    font-size: 15px;
    font-weight: 400;
    letter-spacing: 0.6px;
    text-transform: uppercase;
  }
  .contact {
    margin-top: 46px;
  }
  .contact__name {
    margin-left: 60px;
    font-size: 17px;
    font-weight: 500;
    letter-spacing: 0.8px;
    text-transform: uppercase;
  }
  .contact__line {
    margin-top: 8px;
    font-size: 14.5px;
    font-weight: 300;
    letter-spacing: 0.3px;
  }
  .website {
    margin: 52px 0 0 36px;
    font-size: 17px;
    font-weight: 300;
    letter-spacing: 0.4px;
  }
</style>
</head>
<body>
<main class="stage">
  <section class="card card--front" aria-label="Business card front">
    <div class="card__content">
      <div class="wordmark"><span class="wordmark__square"></span><span>Velmira Candles</span></div>
      <p class="tagline">Hand-Poured Eco Soy Candles</p>
      <div class="contact">
        <p class="contact__name">Lorraine Quibell</p>
        <p class="contact__line">T. 0438.276.904 · info@velmirawicks.com.au</p>
      </div>
    </div>
  </section>

  <section class="card card--back" aria-label="Business card back">
    <div class="card__content">
      <div class="wordmark"><span class="wordmark__square"></span><span>Velmira Candles</span></div>
      <p class="tagline">Hand-Poured Eco Soy Candles</p>
      <p class="website">www.velmirawicks.com.au</p>
    </div>
  </section>
</main>
</body>
</html>
```